Finish My Wordpress Site for Local Painting Company

The site is almost done, but I'm stuck and need expert assistance. Would love to work with someone over zoom so that I can express what I've been trying to accomplish and to learn more about the back end of Wordpress. Here's what's left to be done (I think):

Upload New Photos
Gallery (Before&After)
Anchors to: Get a Quote, Gallery
Font consistency
More padding at the bottom of pages?
Edit padding on Contact page?
Links (photos, buttons, social), add domains, edit page names
Normal entrance animation?
Mobile version

And here's the site as is:
http://kv4.c17.webvaultdemo.com/

Coding

Coded - Design and coding required

Number of Pages Required

1 page

Colors
0355a3

Requirements
Must have
• Communication between us as the work gets done

```html
<!DOCTYPE html>
<html lang="en">
<head>
<meta charset="utf-8">
<title>Ned Harlow Painting</title>
<link rel="stylesheet" href="https://fonts.googleapis.com/css2?family=Playfair+Display:ital,wght@0,400;0,700;0,900;1,700&family=Montserrat:wght@400;500;600;700&family=Open+Sans:wght@400;600&display=swap">
<style>
:root{
  --navy:#22288f;
  --blue:#0355a3;
  --deep:#0c3a74;
  --deeper:#08284f;
  --tan:#9b8472;
  --brown:#856a50;
  --btn:#8a6d52;
  --paper:#eef0f3;
  --white:#ffffff;
}
*{box-sizing:border-box;margin:0;padding:0}
html,body{width:1200px;height:3297px;overflow:hidden}
body{position:relative;font-family:"Montserrat",sans-serif;color:var(--white);background:var(--white)}
.abs{position:absolute}
.serif{font-family:"Playfair Display",serif}
.center{left:0;width:1200px;text-align:center}

/* header */
.top-bar{top:0;left:0;width:1200px;height:133px;background:linear-gradient(#f2f3f6,#e6e9ee)}
.contact-mini{top:75px;font-size:11px;color:var(--navy);display:flex;align-items:center;gap:5px}
.brand-badge{top:10px;left:549px;width:102px;height:102px;border-radius:50%;background:var(--navy);border:4px solid var(--white);box-shadow:0 0 0 2px var(--navy);display:flex;align-items:center;justify-content:center;font-family:"Playfair Display",serif;font-weight:700;font-size:15px;color:var(--white);text-align:center;line-height:1.1}
.quote-pill{top:60px;left:834px;width:152px;height:31px;border-radius:16px;background:var(--btn);color:var(--white);font-family:"Playfair Display",serif;font-style:italic;font-weight:700;font-size:13px;display:flex;align-items:center;justify-content:center}
.main-nav{top:133px;left:0;width:1200px;height:49px;background:var(--navy);display:flex;justify-content:center;padding-left:0}
.main-nav a{display:flex;align-items:center;padding:0 24px;font-family:"Playfair Display",serif;font-size:13px;color:var(--white);text-decoration:none}
.main-nav a.active{background:var(--btn);padding:0 35px}

/* hero */
.hero{top:182px;left:0;width:1200px;height:515px;background:linear-gradient(180deg,#4f7ec4 0%,#8fb0d9 35%,#5c7f7a 60%,#3f5f5a 100%)}
.hero-title{top:452px;font-family:"Playfair Display",serif;font-weight:900;font-size:82px;color:var(--white);text-shadow:0 3px 6px rgba(0,0,0,.35)}
.hero-sub{top:548px;font-size:22px;font-weight:500;letter-spacing:.5px;color:var(--white)}
.hero-btn{top:601px;left:500px;width:199px;height:39px;border-radius:20px;background:var(--btn);font-family:"Playfair Display",serif;font-size:14px;display:flex;align-items:center;justify-content:center}

/* sections */
.band{left:0;width:1200px}
.tan{background:var(--tan)}
.brown{background:var(--brown)}
.eyebrow{font-size:13px}
.sec-title{font-family:"Playfair Display",serif;font-weight:700;font-size:22px}
.welcome-icon{top:711px;left:573px;width:54px;height:54px;border-radius:50%;background:var(--white);display:flex;align-items:center;justify-content:center}
.welcome-copy{top:852px;left:252px;width:696px;font-family:"Open Sans",sans-serif;font-size:10px;line-height:19px;text-align:center}
.welcome-copy p+p{margin-top:18px}
.pill{height:40px;border-radius:20px;background:var(--btn);display:flex;align-items:center;justify-content:center;font-size:12px;letter-spacing:.5px}

.card{top:1204px;height:202px;background:var(--white);padding:3px}
.card .ph{height:143px}
.card h3{font-family:"Playfair Display",serif;font-weight:700;font-size:16px;color:#2c2c2c;text-align:center;margin-top:17px}

.svc{font-size:13px;font-weight:600;display:flex;align-items:center;gap:10px}

.roundel{top:1875px;width:172px;height:172px;border-radius:50%;border:5px solid var(--white)}
.cap{top:2063px;width:200px;font-size:13px;text-align:center;line-height:15px}

.t-title{top:2208px;font-size:24px;font-weight:700;color:var(--blue)}
.t-card{top:2285px;height:135px;background:var(--white);box-shadow:0 0 6px rgba(0,0,0,.22);padding:18px 9px;color:var(--blue)}
.t-head{display:flex;gap:8px;align-items:center}
.t-av{width:20px;height:20px;border-radius:50%;background:#c9ced6}
.t-name{font-family:"Playfair Display",serif;font-weight:700;font-size:9px}
.stars{font-size:8px;letter-spacing:1px}
.t-text{margin-top:18px;font-size:10px;line-height:15px}
.arrow{top:2338px;width:27px;height:27px;border-radius:50%;background:var(--blue);display:flex;align-items:center;justify-content:center}

.social{width:32px;height:32px;border-radius:50%;background:var(--white)}
.footer-dot{width:24px;height:24px;border-radius:50%;background:#2a8ae8}

.field{left:587px;width:317px;background:var(--white);border:1px solid #4f6a9a;font-size:10px;color:#888;padding:8px}
.ic-circle{width:38px;height:38px;border-radius:50%;background:var(--white);display:flex;align-items:center;justify-content:center}
.big-contact{font-family:"Playfair Display",serif;font-size:17px}

.foot-text{font-size:9px;line-height:15px}
</style>
</head>
<body>

<header>
  <div class="abs top-bar"></div>
  <div class="abs contact-mini" style="left:212px">
    <svg width="10" height="10" viewBox="0 0 24 24"><path fill="#22288f" d="M6.6 10.8a15 15 0 0 0 6.6 6.6l2.2-2.2a1 1 0 0 1 1-.25 11.4 11.4 0 0 0 3.6.6 1 1 0 0 1 1 1V20a1 1 0 0 1-1 1A17 17 0 0 1 3 4a1 1 0 0 1 1-1h3.5a1 1 0 0 1 1 1 11.4 11.4 0 0 0 .6 3.6 1 1 0 0 1-.25 1z"/></svg>
    (555) 014-2287
  </div>
  <div class="abs contact-mini" style="left:324px">
    <svg width="11" height="9" viewBox="0 0 24 18"><rect x="1" y="1" width="22" height="16" fill="none" stroke="#22288f" stroke-width="2"/><path d="M1 1l11 9 11-9" fill="none" stroke="#22288f" stroke-width="2"/></svg>
    ned@harlowpaintco.com
  </div>
  <div class="abs brand-badge">Ned<br>Harlow</div>
  <div class="abs quote-pill">Get A Free Quote</div>
  <nav class="abs main-nav">
    <a class="active" href="#">Home</a><a href="#">About</a><a href="#">Services</a><a href="#">Gallery</a><a href="#">Reviews</a><a href="#">Blog</a><a href="#">Contact</a>
  </nav>
</header>

<section>
  <div class="abs hero" role="img" aria-label="Photo of a painted Victorian house with a round tower under a blue sky"></div>
  <h1 class="abs center hero-title">Ned Harlow Painting</h1>
  <div class="abs center hero-sub">WHERE PREPARATION MAKES ALL THE DIFFERENCE</div>
  <div class="abs hero-btn">GET A FREE QUOTE</div>
</section>

<section>
  <div class="abs band tan" style="top:697px;height:453px"></div>
  <div class="abs welcome-icon">
    <svg width="28" height="28" viewBox="0 0 24 24" fill="none" stroke="#9b8472" stroke-width="1.6" stroke-linejoin="round"><path d="M14 4l6 6-5 5-6-6z"/><path d="M11 11l-5 5-2 4 4-2 5-5"/></svg>
  </div>
  <div class="abs center eyebrow" style="top:774px">welcome to</div>
  <h2 class="abs center sec-title" style="top:795px">Ned Harlow Painting</h2>
  <div class="abs welcome-copy">
    <p>At Ned Harlow's, we offer an array of paint services in the Cambridge, Waltham, and Metrowest areas. Our preparation is unparalleled, and we use nothing short of the best methods so that you can sit down and relax with a glass of lemonade, knowing that all your concerns are going to be taken care of by an expert painter you can trust.</p>
    <p>We have reliable systems that help us to avoid mistakes, address every concern, and ensure your job runs seamlessly. We are lead safe certified and use environmentally friendly, zero VOC products to complete all our projects. Our crisp lines, attention to detail, personalized customer service, and competitive rates make Ned Harlow's the most unrivaled painting company you will find in the area and the best choice for all your painting needs.</p>
  </div>
  <div class="abs pill" style="top:1045px;left:526px;width:148px">READ MORE</div>
</section>

<section>
  <div class="abs band brown" style="top:1150px;height:324px"></div>
  <div class="abs card" style="left:242px;width:225px"><div class="ph" role="img" aria-label="Photo of a brush painting white trim" style="background:linear-gradient(90deg,#8e9296,#e6e8e8 40%,#cfd1d0 80%,#5d5f60)"></div><h3>Kitchen Cabinet</h3></div>
  <div class="abs card" style="left:490px;width:223px"><div class="ph" role="img" aria-label="Photo of a clipboard quote form on a wooden bench" style="background:linear-gradient(135deg,#6b5534,#b9a37c 45%,#e4e3de 60%,#7d6642)"></div><h3 style="margin-top:15px">Get A Quote</h3></div>
  <div class="abs card" style="left:729px;width:224px"><div class="ph" role="img" aria-label="Photo of green evergreen shrubs" style="background:linear-gradient(160deg,#3f6e1e,#6fa535 50%,#2f5a17)"></div><h3>Testimonials</h3></div>
</section>

<section>
  <div class="abs band tan" style="top:1474px;height:277px"></div>
  <div class="abs center eyebrow" style="top:1500px">services</div>
  <h2 class="abs center sec-title" style="top:1518px">Explore Our Services</h2>
  <svg width="0" height="0" style="position:absolute"><symbol id="tick" viewBox="0 0 16 16"><circle cx="8" cy="8" r="6.5" fill="none" stroke="#fff" stroke-width="1.2"/><path d="M5 8l2.2 2.2L13 4" fill="none" stroke="#fff" stroke-width="1.4"/></symbol></svg>
  <div class="abs svc" style="left:308px;top:1606px"><svg width="15" height="15"><use href="#tick"/></svg>Interior</div>
  <div class="abs svc" style="left:308px;top:1634px"><svg width="15" height="15"><use href="#tick"/></svg>Presure Wash</div>
  <div class="abs svc" style="left:308px;top:1662px"><svg width="15" height="15"><use href="#tick"/></svg>Kitchen Cabinets</div>
  <div class="abs svc" style="left:527px;top:1606px"><svg width="15" height="15"><use href="#tick"/></svg>Exterior</div>
  <div class="abs svc" style="left:527px;top:1634px"><svg width="15" height="15"><use href="#tick"/></svg>commercial</div>
  <div class="abs svc" style="left:527px;top:1662px"><svg width="15" height="15"><use href="#tick"/></svg>Graffitti Removal</div>
  <div class="abs svc" style="left:746px;top:1606px"><svg width="15" height="15"><use href="#tick"/></svg>Carpentry</div>
  <div class="abs svc" style="left:746px;top:1634px"><svg width="15" height="15"><use href="#tick"/></svg>EMF Shielding</div>
  <div class="abs svc" style="left:746px;top:1662px"><svg width="15" height="15"><use href="#tick"/></svg>Faux &amp; Decorative</div>
</section>

<section>
  <div class="abs band brown" style="top:1751px;height:398px"></div>
  <div class="abs center eyebrow" style="top:1777px">no matter the job</div>
  <h2 class="abs center sec-title" style="top:1795px">Ned Harlow's will Make it Happen.</h2>
  <div class="abs roundel" style="left:311px" role="img" aria-label="Photo of paint brushes on a pegboard" style-note="" ></div>
  <div class="abs roundel" style="left:515px;background:radial-gradient(circle,#c9a24a 0 45%,#1d2553 47% 100%)" role="img" aria-label="Satisfaction guarantee seal"></div>
  <div class="abs roundel" style="left:720px;background:linear-gradient(135deg,#2c5a74,#4e8aa6 50%,#23485c)" role="img" aria-label="Illustration of a painter rolling paint on a brick wall"></div>
  <div class="abs cap" style="left:297px">Painters &amp; Carpenters<br>You can Trust</div>
  <div class="abs cap" style="left:501px;top:2066px">100% Satisfaction<br>Guranteed</div>
  <div class="abs cap" style="left:706px;top:2068px">Lets Talk<br>Painting</div>
</section>
<style>.roundel[aria-label^="Photo of paint"]{background:linear-gradient(135deg,#d7b57a,#27407a 50%,#c89a55)}</style>

<section>
  <div class="abs center eyebrow" style="top:2186px;color:#555">testimonials</div>
  <h2 class="abs center t-title">WHAT CLIENTS SAYS ABOUT US</h2>
  <div class="abs arrow" style="left:161px"><svg width="12" height="12" viewBox="0 0 12 12"><path d="M10 6H2M5.5 2.5L2 6l3.5 3.5" fill="none" stroke="#fff" stroke-width="1.8"/></svg></div>
  <div class="abs t-card" style="left:221px;width:360px">
    <div class="t-head"><div class="t-av"></div><div><div class="t-name">Mara L.</div><div class="stars">★★★★★</div></div></div>
    <div class="t-text" style="margin-top:22px">Best Painter in Waltham and surrounding towns! Quality work, professional company, timely manner, great prices! Highly recommend!</div>
  </div>
  <div class="abs t-card" style="left:615px;width:360px">
    <div class="t-head"><div class="t-av"></div><div><div class="t-name">Glen P.</div><div class="stars">★★★★★</div></div></div>
    <div class="t-text">We have worked with Ned for many years. His work is first rate. A professional crew that leaves the site in pristine shape. A pleasure to work with them on both interior and exterior projects!</div>
  </div>
  <div class="abs arrow" style="left:1012px"><svg width="12" height="12" viewBox="0 0 12 12"><path d="M2 6h8M6.5 2.5L10 6 6.5 9.5" fill="none" stroke="#fff" stroke-width="1.8"/></svg></div>
</section>

<section>
  <div class="abs" style="top:2474px;left:0;width:600px;height:148px;background:var(--blue)"></div>
  <div class="abs" style="top:2474px;left:600px;width:600px;height:148px;background:linear-gradient(90deg,#0a4585,#06386d)"></div>
  <div class="abs" style="top:2482px;left:300px;width:261px;text-align:right;font-size:22px;font-weight:700">Follow, Like</div>
  <div class="abs" style="top:2512px;left:300px;width:261px;text-align:right;font-size:12px;font-weight:500">&amp; leave us a review</div>
  <div class="abs social" style="top:2557px;left:422px" aria-label="Review site"></div>
  <div class="abs social" style="top:2557px;left:458px" aria-label="Social page"></div>
  <div class="abs social" style="top:2557px;left:493px" aria-label="Listing page"></div>
  <div class="abs social" style="top:2557px;left:529px" aria-label="Professional network"></div>
  <div class="abs" style="top:2482px;left:636px;font-size:22px;font-weight:700">Subscribe</div>
  <div class="abs" style="top:2512px;left:636px;font-size:12px;font-weight:500">get weekly, monthly updates</div>
  <div class="abs" style="top:2556px;left:636px;width:224px;height:37px;background:var(--white);color:#999;font-size:10px;padding:12px 9px">your email id</div>
  <div class="abs" style="top:2556px;left:860px;width:88px;height:37px;background:#111;font-size:10px;font-weight:700;display:flex;align-items:center;justify-content:center">SUBSCRIBE</div>
</section>

<section>
  <div class="abs band brown" style="top:2622px;height:423px"></div>
  <div class="abs center eyebrow" style="top:2664px">call, email or fill the form</div>
  <h2 class="abs center" style="top:2682px;font-size:24px;font-weight:700">GET A FREE QUOTE</h2>
  <div class="abs ic-circle" style="top:2799px;left:281px"><svg width="16" height="16" viewBox="0 0 24 24"><path fill="#856a50" d="M6.6 10.8a15 15 0 0 0 6.6 6.6l2.2-2.2a1 1 0 0 1 1-.25 11.4 11.4 0 0 0 3.6.6 1 1 0 0 1 1 1V20a1 1 0 0 1-1 1A17 17 0 0 1 3 4a1 1 0 0 1 1-1h3.5a1 1 0 0 1 1 1 11.4 11.4 0 0 0 .6 3.6 1 1 0 0 1-.25 1z"/></svg></div>
  <div class="abs big-contact" style="top:2806px;left:335px">(555) 014-2287</div>
  <div class="abs ic-circle" style="top:2863px;left:281px"><svg width="16" height="13" viewBox="0 0 24 18"><rect x="1" y="1" width="22" height="16" fill="none" stroke="#856a50" stroke-width="2"/><path d="M1 1l11 9 11-9" fill="none" stroke="#856a50" stroke-width="2"/></svg></div>
  <div class="abs big-contact" style="top:2870px;left:335px">ned@harlowpaintco.com</div>
  <div class="abs field" style="top:2766px;height:31px">name</div>
  <div class="abs field" style="top:2802px;height:30px">email</div>
  <div class="abs field" style="top:2839px;height:30px">phone no</div>
  <div class="abs field" style="top:2877px;height:72px">requirements in details</div>
  <div class="abs field" style="top:2959px;left:587px;width:92px;height:29px;color:#555;font-weight:600">SEND</div>
</section>

<footer>
  <div class="abs band" style="top:3045px;height:232px;background:var(--deep)"></div>
  <div class="abs band" style="top:3277px;height:20px;background:var(--deeper);font-size:8px;text-align:center;padding-top:5px;letter-spacing:.3px">© 2020, ALL RIGHTS RESERVED, NED HARLOW PAINTING</div>
  <div class="abs" style="top:3082px;left:220px;font-size:14px;font-weight:500">NED HARLOW PAINTING©</div>
  <div class="abs foot-text" style="top:3118px;left:220px;width:260px">Serving Cambridge, Waltham, Arlington, Lincoln, Belmont, Newton, Watertown, Weston, Dover, Winchester, Medford, and Lexington areas.</div>
  <div class="abs footer-dot" style="top:3185px;left:219px"></div>
  <div class="abs footer-dot" style="top:3185px;left:255px"></div>
  <div class="abs footer-dot" style="top:3185px;left:292px"></div>
  <svg class="abs" style="top:3122px;left:526px" width="10" height="10" viewBox="0 0 10 10"><circle cx="5" cy="5" r="4" fill="none" stroke="#fff"/><path d="M5 2.5V5h2" fill="none" stroke="#fff"/></svg>
  <div class="abs foot-text" style="top:3119px;left:544px">MON-FRI: 7AM-7PM<br>SAT-SUN: Closed</div>
  <svg class="abs" style="top:3168px;left:526px" width="10" height="10" viewBox="0 0 24 24"><path fill="#fff" d="M6.6 10.8a15 15 0 0 0 6.6 6.6l2.2-2.2a1 1 0 0 1 1-.25 11.4 11.4 0 0 0 3.6.6 1 1 0 0 1 1 1V20a1 1 0 0 1-1 1A17 17 0 0 1 3 4a1 1 0 0 1 1-1h3.5a1 1 0 0 1 1 1 11.4 11.4 0 0 0 .6 3.6 1 1 0 0 1-.25 1z"/></svg>
  <div class="abs foot-text" style="top:3165px;left:544px">(555) 014-2287</div>
  <svg class="abs" style="top:3187px;left:526px" width="10" height="8" viewBox="0 0 24 18"><rect x="1" y="1" width="22" height="16" fill="none" stroke="#fff" stroke-width="2"/><path d="M1 1l11 9 11-9" fill="none" stroke="#fff" stroke-width="2"/></svg>
  <div class="abs foot-text" style="top:3183px;left:544px">ned@harlowpaintco.com</div>
  <svg class="abs" style="top:3204px;left:526px" width="10" height="10" viewBox="0 0 10 10"><circle cx="5" cy="5" r="4" fill="none" stroke="#fff"/><path d="M1 5h8M5 1c2 2 2 6 0 8M5 1c-2 2-2 6 0 8" fill="none" stroke="#fff" stroke-width=".8"/></svg>
  <div class="abs foot-text" style="top:3201px;left:544px">www.harlowpaintco.com</div>
  <svg class="abs" style="top:3122px;left:682px" width="9" height="12" viewBox="0 0 10 14"><path fill="#fff" d="M5 0a5 5 0 0 1 5 5c0 4-5 9-5 9S0 9 0 5a5 5 0 0 1 5-5z"/><circle cx="5" cy="5" r="1.8" fill="#0c3a74"/></svg>
  <div class="abs foot-text" style="top:3112px;left:711px">18 Linden Row, 2A<br>Cambridge, MA 02100</div>
  <svg class="abs" style="top:3162px;left:682px" width="9" height="12" viewBox="0 0 10 14"><path fill="#fff" d="M5 0a5 5 0 0 1 5 5c0 4-5 9-5 9S0 9 0 5a5 5 0 0 1 5-5z"/><circle cx="5" cy="5" r="1.8" fill="#0c3a74"/></svg>
  <div class="abs foot-text" style="top:3152px;left:711px">402 Orchard Lane, #6<br>Waltham, MA 02400</div>
  <div class="abs brand-badge" style="top:3089px;left:860px;width:128px;height:128px;font-size:19px">Ned<br>Harlow</div>
</footer>

</body>
</html>
```